Storm Restoration Contractor needs a professional letterhead design

Looking for a professional letterhead design. Not looking for your cheapo MS Word standard ones that are readily available. Dont want it to be cookie cutter look like ones readily available online. We just recently changed our logo and want to freshen up all our documents. Our company handles restoring a property back to a pre-loss condition after a storm damages it. For example, wind, hail, flood, fire losses.

Target Market(s)

Property Owners, Homeowners, Property Owners, Commercial Property Owners, Property Management Companies

Industry/Entity Type

Construction Company

Requirements
Must have
• Professional, Use 1 of 2 logo options
• Storm Restoration, Roofing, Siding, Windows

```html
<!DOCTYPE html>
<html lang="en">
<head>
<meta charset="utf-8">
<title>Ridgeline Exteriors Letterhead</title>
<link href="https://fonts.googleapis.com/css2?family=Questrial&display=swap" rel="stylesheet">
<style>
  :root {
    --backdrop: #c4c4c4;
    --paper: #f1f1f1;
    --brand-blue: #2269ae;
    --deep-blue: #1b5590;
    --ink: #4a4a4a;
    --charcoal: #4d4d4d;
    --light-gray: #c9c9c9;
  }
  * { margin: 0; padding: 0; box-sizing: border-box; }
  html, body {
    width: 1200px;
    height: 1041px;
    overflow: hidden;
    background: var(--backdrop);
    font-family: "Questrial", sans-serif;
  }
  .letterhead {
    position: absolute;
    left: 280px;
    top: 106px;
    width: 640px;
    height: 827px;
    background: var(--paper);
    box-shadow: 0 2px 6px rgba(0,0,0,0.25);
  }
  .brand {
    position: absolute;
    left: 50px;
    top: 46px;
    display: flex;
    align-items: center;
    gap: 12px;
  }
  .brand-mark {
    width: 54px;
    height: 54px;
    border-radius: 50%;
    border: 5px solid var(--brand-blue);
  }
  .brand-name {
    color: var(--brand-blue);
    font-size: 22px;
    line-height: 1.05;
    letter-spacing: 2px;
    text-transform: uppercase;
  }
  .contact {
    position: absolute;
    left: 474px;
    top: 54px;
    color: var(--ink);
    font-size: 8.5px;
    line-height: 11.2px;
  }
  .contact-line {
    display: flex;
    align-items: center;
    gap: 5px;
  }
  .contact-icon {
    width: 8px;
    height: 8px;
  }
  .address {
    margin-top: 5px;
  }
  .footer-band {
    position: absolute;
    left: 0;
    bottom: 0;
    width: 640px;
    height: 27px;
  }
  .website {
    position: absolute;
    right: 51px;
    top: 798px;
    font-size: 8px;
    letter-spacing: 0.4px;
    color: var(--ink);
  }
  .website strong {
    color: var(--brand-blue);
    font-weight: normal;
  }
</style>
</head>
<body>
  <main class="letterhead">
    <header class="brand">
      <div class="brand-mark"></div>
      <div class="brand-name">Ridgeline<br>Exteriors</div>
    </header>

    <address class="contact" style="font-style:normal">
      <div class="contact-line">
        <svg class="contact-icon" viewBox="0 0 10 10"><rect width="10" height="10" rx="1.5" fill="var(--brand-blue)"/><path d="M3 2.2 L4.2 3.6 L3.6 4.4 Q4.5 6 5.8 6.5 L6.5 5.9 L7.9 7 L7.2 8 Q4.6 7.8 2.3 3.2 Z" fill="#fff"/></svg>
        <span>555-014-2200</span>
      </div>
      <div class="contact-line">
        <svg class="contact-icon" viewBox="0 0 10 10"><rect width="10" height="10" rx="1.5" fill="var(--brand-blue)"/><rect x="3" y="1.8" width="4" height="2.4" fill="#fff"/><rect x="2" y="4.4" width="6" height="2.6" fill="#fff"/><rect x="3" y="7.2" width="4" height="1.2" fill="#fff"/></svg>
        <span>555-014-2200</span>
      </div>
      <div class="contact-line">
        <svg class="contact-icon" viewBox="0 0 10 10"><rect width="10" height="10" rx="1.5" fill="var(--brand-blue)"/><rect x="2" y="3" width="6" height="4.2" fill="#fff"/><path d="M2 3 L5 5.4 L8 3" stroke="var(--brand-blue)" stroke-width="0.7" fill="none"/></svg>
        <span>info@ridgelineext.com</span>
      </div>
      <div class="address">
        4120 N Canyon Road STE 210<br>
        Mesa, AZ 85201
      </div>
    </address>

    <div class="website">WWW.<strong>RIDGELINEEXT</strong>.COM</div>

    <svg class="footer-band" viewBox="0 0 640 27" preserveAspectRatio="none" aria-hidden="true">
      <polygon points="432,18 640,18 640,27 424,27" fill="var(--charcoal)"/>
      <polygon points="441,9 460,9 441,27 414,27" fill="var(--light-gray)"/>
      <polygon points="0,0 436,0 410,27 0,27" fill="var(--brand-blue)"/>
      <polygon points="326,9 428,9 410,27 310,27" fill="var(--deep-blue)"/>
    </svg>
  </main>
</body>
</html>
```